Exclusive Offer Verbalis December 2022

A design that includes the company logo company and the text set out below. It could be a season design (winter design). it is a short promo to be sent by email. It should express that the promotion is on translation services.

Title: ESPECIAL DICIEMBRE

Information:

10% Descuento del 13 al 16 de diciembre
8% Después del 13 y hasta el 24 de diciembre

En contenidos web, materiales publicitarios, catàlogos, textos legales, manuales y más.

+30 años de experiencia, ISO 17100, traductores nativos

Target Market(s)

B2B Spain - any company that needs translation services

Industry/Entity Type

Services and Translation

Requirements
Must have
• Please take into account our corporate style guide attached
Nice to have
• A design that suggests a special offer from a serious, professional, technological and solid translation company.
Should not have
• Typical Christmas stationery, colours that don't fit into our company design trend.

```html
<!DOCTYPE html>
<html lang="es">
<head>
<meta charset="utf-8">
<title>Especial Diciembre – Verbalis</title>
<link rel="stylesheet" href="https://fonts.googleapis.com/css2?family=Montserrat:wght@300;400;500;600;700;800&display=swap">
<style>
  :root {
    --navy: #1c4479;
    --orange: #e07b22;
    --white: #ffffff;
    --ink: #2a3550;
    --stage: #ececec;
    --photo-light: #e4eaf1;
    --photo-mid: #aab7c7;
    --photo-dark: #4c5868;
  }
  html, body {
    margin: 0;
    padding: 0;
    width: 1200px;
    height: 581px;
    overflow: hidden;
    background: var(--stage);
  }
  .promo-canvas {
    position: relative;
    width: 1200px;
    height: 581px;
  }
  .promo-banner {
    position: absolute;
    left: 0;
    top: 66px;
    width: 1200px;
    height: 448px;
    display: block;
    font-family: "Montserrat", sans-serif;
  }
  .title-light { fill: var(--navy); font-weight: 400; font-size: 56px; }
  .title-bold { fill: var(--orange); font-weight: 800; font-size: 56px; }
  .tab-label { fill: var(--orange); font-weight: 600; font-size: 22px; }
  .discount-figure { fill: var(--white); font-weight: 700; font-size: 112px; }
  .discount-tag { fill: var(--white); font-weight: 500; font-size: 28px; }
  .discount-dates { fill: var(--white); font-weight: 500; font-size: 32px; }
  .second-offer { fill: var(--white); font-weight: 400; font-size: 22px; }
  .service-list { fill: var(--white); font-weight: 400; font-size: 21px; }
  .service-dot { fill: var(--orange); }
  .arc-label { fill: var(--white); font-weight: 500; font-size: 17px; }
  .credentials { fill: var(--ink); font-weight: 400; font-size: 15.5px; }
  .web-address { font-weight: 500; font-size: 15.5px; fill: var(--ink); }
  .web-address .web-name { fill: var(--orange); font-weight: 600; }
  .brand-name { fill: var(--navy); font-weight: 700; font-size: 30px; letter-spacing: 1px; }
</style>
</head>
<body>
<main class="promo-canvas">
  <svg class="promo-banner" viewBox="0 0 1200 448" xmlns="http://www.w3.org/2000/svg">
    <defs>
      <linearGradient id="photoTone" x1="0" y1="0" x2="1" y2="1">
        <stop offset="0" stop-color="var(--photo-light)"/>
        <stop offset="0.55" stop-color="var(--photo-mid)"/>
        <stop offset="1" stop-color="var(--photo-dark)"/>
      </linearGradient>
      <clipPath id="bannerClip"><rect width="1200" height="448"/></clipPath>
      <path id="serviceArc" d="M 316.9 340.4 A 226 226 0 0 0 395.4 135.8"/>
    </defs>

    <g clip-path="url(#bannerClip)">
      <rect class="banner-ground" width="1200" height="448" fill="var(--white)"/>

      <!-- offer band -->
      <polygon class="offer-band" points="0,96 1200,96 1200,332 900,332 870,363 0,363" fill="var(--navy)"/>
      <polygon class="offer-tab" points="731,96 940,96 932,118 737,118" fill="var(--white)"/>

      <!-- photo area -->
      <circle class="photo-frame" cx="171.6" cy="163" r="206" fill="url(#photoTone)" role="img" aria-label="Photo: business handshake over a desk with documents"/>

      <!-- accent arcs -->
      <path class="accent-arc" d="M 329.4 0 A 230 230 0 0 1 398.1 127.3" fill="none" stroke="var(--orange)" stroke-width="2"/>
      <path class="accent-arc" d="M 310 351 A 230 230 0 0 1 0 320.3" fill="none" stroke="var(--orange)" stroke-width="2"/>

      <text class="arc-label"><textPath href="#serviceArc" startOffset="50%" text-anchor="middle">Translation Services</textPath></text>
    </g>

    <!-- headline -->
    <text class="title-light" x="476" y="67" textLength="279" lengthAdjust="spacingAndGlyphs">ESPECIAL</text>
    <text class="title-bold" x="772" y="67" textLength="336" lengthAdjust="spacingAndGlyphs">DICIEMBRE</text>
    <text class="tab-label" x="745" y="113" textLength="175" lengthAdjust="spacingAndGlyphs">Exclusive Offer</text>

    <!-- main discount -->
    <text class="discount-figure" x="481" y="202" textLength="204" lengthAdjust="spacingAndGlyphs">10%</text>
    <rect class="discount-box" x="685" y="172" width="171" height="31" fill="var(--orange)"/>
    <text class="discount-tag" x="695" y="198" textLength="148" lengthAdjust="spacingAndGlyphs">Descuento</text>
    <text class="discount-dates" x="488" y="247" textLength="370" lengthAdjust="spacingAndGlyphs">del 13 al 16 de diciembre</text>

    <line class="offer-divider" x1="895" y1="173" x2="895" y2="249" stroke="var(--white)" stroke-opacity="0.45" stroke-width="1.5"/>
    <text class="second-offer" x="931" y="190">8% Después del</text>
    <text class="second-offer" x="931" y="218">13 y hasta el</text>
    <text class="second-offer" x="931" y="245">24 de diciembre</text>

    <!-- services -->
    <text class="service-list" x="799" y="290" text-anchor="middle">EN Contenidos web <tspan class="service-dot">●</tspan> Materiales publicitarios <tspan class="service-dot">●</tspan> Catàlogos</text>
    <text class="service-list" x="799" y="318" text-anchor="middle">Textos legales <tspan class="service-dot">●</tspan> Manuales <tspan class="service-dot">●</tspan> y más.</text>

    <!-- footer -->
    <text class="credentials" x="371" y="405">+30 years of experience,</text>
    <text class="credentials" x="371" y="427">ISO 17100, native translators</text>
    <line class="footer-divider" x1="606" y1="390" x2="606" y2="429" stroke="var(--ink)" stroke-opacity="0.35" stroke-width="1.2"/>
    <text class="web-address" x="625" y="408" textLength="240" lengthAdjust="spacingAndGlyphs">www.<tspan class="web-name">verbalis-translations</tspan>.co.uk</text>

    <!-- brand -->
    <circle class="brand-dot" cx="966" cy="394" r="15" fill="var(--navy)"/>
    <text class="brand-name" x="992" y="405">VERBALIS</text>
  </svg>
</main>
</body>
</html>
```